Trendy E Juice Product Labels Required

We are looking for design for an e Juice label line (the liquids used in electronic cigarettes). What we need is 5 product labels which eventually will be printed on 95mm x 40mm labels. Obviously the image will be created much larger than this but the aspect ratio should be scalable down to this size.

What each label must have is I would need is a background, a monster character, and space for a product name incorporated in to the design. The brand on this line is "Brisk Lantern". Whilst creatively, we are completely open to any concept, there is certain text which is necessary for incorporation in to each label. The attached file, "Example Label" shows these elements. NOTE: the attached file IS NOT a finished label.
Updates

Project Deadline Extended
Reason: Not received a design that we wish to proceed with.

Target Market(s)

25-35 year old vapers

Industry/Entity Type

Electronic

Requirements
Should not have
• Anything that may be construed as being targeted toward children.

```html
<!DOCTYPE html>
<html lang="en">
<head>
<meta charset="utf-8">
<title>Brisk Lantern – E-Liquid Label</title>
<link rel="stylesheet" href="https://fonts.googleapis.com/css2?family=Barlow:ital,wght@0,400;0,500;0,700;0,800;1,400&display=swap">
<style>
  :root {
    --violet: #5b4a9e;
    --ink: #000000;
    --paper: #ffffff;
    --pattern-dark: #2a2a2a;
    --pattern-light: #8a8a8a;
  }
  * { box-sizing: border-box; margin: 0; padding: 0; }
  html, body { width: 1200px; height: 504px; overflow: hidden; background: var(--paper); }
  body { font-family: "Barlow", sans-serif; color: var(--paper); }

  .label { position: relative; width: 1200px; height: 504px; background: var(--ink); overflow: hidden; }
  .band { position: absolute; left: 0; width: 100%; background: var(--violet); z-index: 3; }
  .band--top { top: 0; height: 22px; }
  .band--bottom { bottom: 0; height: 38px; }

  /* left: legal panel */
  .legal { position: absolute; left: 0; top: 22px; width: 340px; height: 444px; padding: 14px 14px 0 14px; }
  .legal h2 { font-weight: 500; font-size: 25px; letter-spacing: 0.5px; line-height: 1; margin-bottom: 4px; }
  .legal p { font-size: 15.6px; line-height: 21.5px; }
  .legal .ingredients-title { margin-top: 21px; }

  /* centre: brand panel */
  .brand { position: absolute; left: 340px; top: 22px; width: 462px; height: 444px; overflow: hidden; }
  .brand__pattern { position: absolute; inset: 0; background: linear-gradient(135deg, var(--pattern-dark), var(--pattern-light) 50%, var(--pattern-dark)); }
  .brand__diamond { position: absolute; left: 73px; top: -4px; width: 316px; height: 316px; background: var(--paper); transform: rotate(45deg); transform-origin: center; top: 70px; }
  .brand__diamond-wrap { position: absolute; inset: 0; }
  .brand__lockup { position: absolute; left: 96px; top: 86px; width: 300px; }
  .brand__name { color: var(--ink); font-weight: 800; font-size: 64px; line-height: 0.98; letter-spacing: 1px; text-transform: uppercase; }
  .brand__mark { position: absolute; left: 232px; top: 0; width: 52px; height: 52px; border-radius: 50%; background: var(--violet); }
  .product-name { position: absolute; left: 97px; top: 309px; width: 274px; height: 50px; background: var(--violet); color: var(--paper); font-size: 34px; font-weight: 400; text-align: center; line-height: 50px; }
  .volume { position: absolute; left: 0; width: 100%; top: 395px; text-align: center; color: var(--ink); font-size: 20px; }

  /* right: contact panel */
  .contact { position: absolute; left: 802px; top: 22px; width: 398px; height: 444px; padding-left: 45px; }
  .contact__lead { font-style: italic; font-size: 17px; margin-top: 38px; }
  .social { display: flex; gap: 33px; margin-top: 14px; margin-left: -6px; }
  .social span { width: 61px; height: 61px; border-radius: 50%; background: var(--violet); }
  .contact__web { font-weight: 700; font-size: 17px; line-height: 25px; margin-top: 20px; }
  .contact__dist { font-size: 16px; line-height: 22.5px; margin-top: 44px; }
  .notices { position: absolute; left: 36px; top: 362px; display: flex; gap: 14px; align-items: center; }
  .notices svg { width: 60px; height: 60px; }
</style>
</head>
<body>
<div class="label">
  <div class="band band--top"></div>

  <section class="legal">
    <h2>WARNING</h2>
    <p>This product contains nicotine, a substance which is known to cause birth defects. Do not swallow. Avoid contact with skin. Keep out of reach of children and pets. This product is intended for use by persons 18 and older. Pregnant women and those breast feeding should not use this product. May contain traces of nuts.</p>
    <h2 class="ingredients-title">INGREDIENTS</h2>
    <p>USP/EP Propelyn Glycol (XX%), USP/EP Vetetable Glycerin (XX%), USP/EP Nicotine, Natural and Artificial Flavorings.</p>
  </section>

  <section class="brand">
    <div class="brand__pattern" role="img" aria-label="Black and white interlaced geometric lattice pattern"></div>
    <div class="brand__diamond"></div>
    <div class="brand__lockup">
      <div class="brand__name">Brisk<br>Lantern</div>
      <div class="brand__mark" role="img" aria-label="Purple monster character mascot"></div>
    </div>
    <div class="product-name">Product Name</div>
    <div class="volume">30ml</div>
  </section>

  <section class="contact">
    <p class="contact__lead">Find us at:</p>
    <div class="social"><span></span><span></span><span></span></div>
    <p class="contact__web">www.brisklantern.com<br>@brisklantern</p>
    <p class="contact__dist">Distributed by:<br>Brisk Lantern<br>Address<br>Telephone</p>
    <div class="notices">
      <svg viewBox="0 0 60 60" aria-label="Recycle"><g fill="none" stroke="#fff" stroke-width="6"><path d="M18 40 L30 18 L42 40 Z"/></g></svg>
      <svg viewBox="0 0 60 60" aria-label="Caution"><path d="M30 4 L57 54 H3 Z" fill="#fff"/><rect x="27" y="20" width="6" height="20" fill="#000"/><rect x="27" y="44" width="6" height="6" fill="#000"/></svg>
      <svg viewBox="0 0 60 60" aria-label="Dispose in bin"><rect x="30" y="24" width="20" height="30" fill="#fff"/><rect x="27" y="18" width="26" height="4" fill="#fff"/><circle cx="14" cy="12" r="5" fill="#fff"/><path d="M14 18 L14 36 M14 24 L28 20 M14 36 L8 54 M14 36 L20 54" stroke="#fff" stroke-width="4" fill="none"/></svg>
      <svg viewBox="0 0 60 60" aria-label="Not for under 18"><circle cx="30" cy="30" r="26" fill="none" stroke="#fff" stroke-width="5"/><text x="30" y="39" text-anchor="middle" font-family="Barlow, sans-serif" font-weight="700" font-size="24" fill="#fff">18</text><line x1="12" y1="12" x2="48" y2="48" stroke="#fff" stroke-width="5"/></svg>
    </div>
  </section>

  <div class="band band--bottom"></div>
</div>
</body>
</html>
```